Digital Billboard Design: Winter Sales Event

I own a boutique furniture store in Calgary, AB (maplecrestdecor.ca) and I am looking to advertise our winter sale event on a new curved digital billboard (specs attached including required file type).

I have this billboard rented for 52-weeks so I will be looking to change the design every 4-weeks (i.e. this is intended to be an ongoing project).

The objective of this first billboard is to raise awareness around our annual winter sales event. The store itself is only a few blocks from the billboard so those commuting into downtown are just a short drive from the store.

I am looking for a fresh, clean, contemporary look that will grab your attention as you drive into downtown Calgary without presenting to much info so as to be distracting (and overwhelming -- the billboard does not need to contain all info on my current marketing material). I should also note that the store caters to a higher-end, more sophisticated clientele so the graphics need to reflect the brand (i.e. we are not Brennick Furniture or Couch Depot!).

I have attached three files:

Billboard specs
Current marketing material advertising sale (and all relevant data)
An idea that is from an American furniture store that I think is interesting

Target Market(s)

Upper middle class, sophisticated client who appreciates the finer things in life.

Industry/Entity Type

Furniture Store

Font styles to use
Sans Serif

Requirements
Must have
• Company Logo
• Winter Sales Event - 20 to 60% off
• Address: 2743 8th Ave SW
Nice to have
• Image of furniture -- see our website www.maplecrestdecor.ca -- any photo from this site can be used
Should not have
• Too much text or visual distration

```html
<!DOCTYPE html>
<html lang="en">
<head>
<meta charset="utf-8">
<title>Maplecrest Decor – Winter Sales Event</title>
<link href="https://fonts.googleapis.com/css2?family=Lato:wght@300;400;700&display=swap" rel="stylesheet">
<style>
  :root {
    --band-top: #e8d170;
    --band-bottom: #f2ea98;
    --floor: #ffffff;
    --floor-shade: #ececec;
    --sale-red: #e8262b;
    --ink-grey: #5f6062;
    --seat-red: #b5241f;
    --frame-grey: #8d8c86;
  }
  * { margin: 0; padding: 0; box-sizing: border-box; }
  html, body { width: 1200px; height: 576px; overflow: hidden; background: var(--floor); }
  .billboard {
    position: relative;
    width: 1200px;
    height: 576px;
    font-family: "Lato", Arial, sans-serif;
    background: var(--floor);
    overflow: hidden;
  }
  .backdrop {
    position: absolute;
    left: 0; top: 0;
    width: 1200px; height: 342px;
    background: linear-gradient(180deg, var(--band-top) 0%, var(--band-bottom) 45%, var(--band-bottom) 100%);
  }
  .floor {
    position: absolute;
    left: 0; top: 342px;
    width: 1200px; height: 234px;
    background: linear-gradient(180deg, var(--floor-shade) 0%, var(--floor) 28%);
  }
  .product-photo {
    position: absolute;
    left: 40px; top: 105px;
    width: 500px; height: 340px;
    border-radius: 6px;
    background:
      linear-gradient(180deg, var(--seat-red) 0%, var(--seat-red) 38%, rgba(141,140,134,0.55) 38%, rgba(141,140,134,0.25) 100%);
  }
  .headline {
    position: absolute;
    right: 62px; top: 186px;
    color: var(--sale-red);
    text-align: right;
    line-height: 1;
  }
  .headline__event {
    font-weight: 300;
    font-size: 50px;
    letter-spacing: 0.5px;
  }
  .headline__event strong { font-weight: 700; font-size: 56px; }
  .headline__discount {
    display: block;
    margin-top: 10px;
    font-weight: 300;
    font-size: 80px;
    letter-spacing: 1px;
  }
  .signature {
    position: absolute;
    right: 62px; top: 398px;
    display: flex;
    align-items: baseline;
    gap: 28px;
    color: var(--ink-grey);
  }
  .signature__brand {
    font-weight: 400;
    font-size: 25px;
    letter-spacing: 4px;
  }
  .signature__address {
    font-weight: 300;
    font-size: 24px;
    letter-spacing: 0.5px;
  }
</style>
</head>
<body>
  <main class="billboard">
    <div class="backdrop"></div>
    <div class="floor"></div>
    <div class="product-photo" role="img" aria-label="Red upholstered bench on a curved chrome X-frame wearing a Santa hat"></div>
    <h1 class="headline">
      <span class="headline__event">WINTER <strong>SALES</strong> EVENT</span>
      <span class="headline__discount">20 to 60% OFF</span>
    </h1>
    <div class="signature">
      <span class="signature__brand">MAPLECREST DECOR</span>
      <span class="signature__address">2743 8th Ave SW</span>
    </div>
  </main>
</body>
</html>
```